Brannigan Schedule Oversight Group Inc. needs a logo design (BSOGI) and a business card design

We need a logo design and business card design for a new company. Simple yet elegant/stylish and professional. to the point. Focal point BRANNIGAN...underneith Schedule Oversight Group Inc smaller font. Plus a logo that can be on the opposite side of the business card and used for T-Shirts.
Back back ground, silver/grey font. I like the look of QVR Design logo
Target Market(s)
Project controls, Planning, Scheduling, Engineering, Project Management
Industry/Entity Type
Business
Contact Information for Business Card
Company name on one side, logo and details on the other
Font styles to use
Requirements
Must have
- Rosalind Brannigan
- Project Planner
- BranniganSOGI@mailnest.example
- P.O. Box 7
- Larkhaven SK CANADA
- T0M2J3
- +1 (403) 555 0187
Nice to have
- Your input :) quote "Fail to plan, plan to fail"
Should not have
- Too much!

```html
<!DOCTYPE html>
<html lang="en">
<head>
<meta charset="utf-8">
<title>Brannigan Schedule Oversight Group Inc. — Business Card</title>
<link rel="stylesheet" href="https://fonts.googleapis.com/css2?family=Mulish:wght@400;700&display=swap">
<style>
  :root {
    --backdrop: #e4e4e2;
    --card-white: #ffffff;
    --card-black: #121212;
    --ink: #1c1c1c;
    --ink-soft: #4a4a4a;
    --silver: #a9a9a9;
  }
  * { box-sizing: border-box; margin: 0; padding: 0; }
  html, body {
    width: 1200px;
    height: 1021px;
    overflow: hidden;
    background: var(--backdrop);
    font-family: "Mulish", sans-serif;
  }
  .canvas { position: relative; width: 1200px; height: 1021px; }

  .card {
    position: absolute;
    width: 640px;
    height: 366px;
    box-shadow: 0 10px 30px rgba(0,0,0,0.18);
  }
  .card--front { left: 90px; top: 110px; background: var(--card-white); color: var(--ink); }
  .card--back  { left: 470px; top: 545px; background: var(--card-black); }

  .wordmark { text-transform: uppercase; font-weight: 700; line-height: 1; }
  .wordmark__name { display: block; letter-spacing: 0.06em; }
  .wordmark__tag { display: block; letter-spacing: 0.08em; }

  .card--front .wordmark { position: absolute; left: 40px; top: 46px; color: var(--ink); }
  .card--front .wordmark__name { font-size: 34px; }
  .card--front .wordmark__tag { font-size: 10.5px; margin-top: 7px; }

  .holder { position: absolute; left: 40px; bottom: 56px; }
  .holder__name { font-size: 22px; font-weight: 700; color: var(--ink-soft); }
  .holder__role { font-size: 14px; color: var(--ink-soft); margin-top: 4px; }

  .contact {
    position: absolute;
    left: 372px;
    top: 44px;
    list-style: none;
    font-size: 13px;
    color: var(--ink);
    line-height: 1.35;
  }
  .contact__item { display: flex; align-items: flex-start; gap: 8px; margin-bottom: 4px; }
  .contact__icon { width: 13px; height: 13px; flex: none; margin-top: 2px; fill: var(--ink-soft); }

  .card--back .wordmark {
    position: absolute;
    left: 0; right: 0;
    top: 50%;
    transform: translateY(-50%);
    text-align: center;
    color: var(--silver);
  }
  .card--back .wordmark__name { font-size: 62px; }
  .card--back .wordmark__tag { font-size: 17px; margin-top: 12px; }
</style>
</head>
<body>
<main class="canvas">
  <section class="card card--front">
    <div class="wordmark">
      <span class="wordmark__name">Brannigan</span>
      <span class="wordmark__tag">Schedule Oversight Group Inc.</span>
    </div>

    <div class="holder">
      <p class="holder__name">Rosalind Brannigan</p>
      <p class="holder__role">Project Planner</p>
    </div>

    <ul class="contact">
      <li class="contact__item">
        <svg class="contact__icon" viewBox="0 0 16 16" aria-hidden="true"><path d="M1 3h14v10H1z M1 3l7 6 7-6" fill="none" stroke="#4a4a4a" stroke-width="1.6"/></svg>
        <span>BranniganSOGI@mailnest.example</span>
      </li>
      <li class="contact__item">
        <svg class="contact__icon" viewBox="0 0 16 16" aria-hidden="true"><path d="M2 5c0-2 2-3 6-3s6 1 6 3v1h-3V5H5v1H2z M4 7h8l2 6H2z"/></svg>
        <span>+1 (403) 555 0187</span>
      </li>
      <li class="contact__item">
        <svg class="contact__icon" viewBox="0 0 16 16" aria-hidden="true"><path d="M8 1a5 5 0 0 0-5 5c0 4 5 9 5 9s5-5 5-9a5 5 0 0 0-5-5zm0 7a2 2 0 1 1 0-4 2 2 0 0 1 0 4z"/></svg>
        <span>P.O. Box 7<br>Larkhaven SK CANADA<br>T0M2J3</span>
      </li>
    </ul>
  </section>

  <section class="card card--back">
    <div class="wordmark">
      <span class="wordmark__name">Brannigan</span>
      <span class="wordmark__tag">Schedule Oversight Group Inc.</span>
    </div>
  </section>
</main>
</body>
</html>
```